Company Website for Zorvel Analytics, an open source data analytics company focused on relationship and li

I need a company/brand website for our new startup, Zorvel Analytics LLC. We are a company focused on using life pattern analysis techniques, looking at relationships and how relationships, attributes, and activity cluster to infer aggregate information about individuals and groups. Our focus is on improving the digital advertising market.

We have a company logo which I will upload shortly.

Target Market(s)

Digital Advertising

Number of Pages Required

3 page

Font styles to use
Sans Serif

Requirements
Must have
• An main page, about us, contact page.
Nice to have
• Zorvel Analytics relies on state of the art analytics applied to a the digital marketing space. While it is heavy in science, we also understand the art of influence. The website should have a scientific edge but also a flair that illustrates our focus on applying the hard science and analytics to influencing the behavior of people.

```html
<!DOCTYPE html>
<html lang="en">
<head>
<meta charset="utf-8">
<title>Zorvel Analytics</title>
<link href="https://fonts.googleapis.com/css2?family=Poppins:wght@400;500;600;700&family=Lato:wght@400;700&display=swap" rel="stylesheet">
<style>
:root{
  --orange:#f6a033;
  --ink:#111111;
  --text:#333333;
  --blue:#2a9fd8;
  --light:#f7f7f7;
  --white:#ffffff;
  --footer:#0b0b0b;
  --muted:#8a8a8a;
}
*{margin:0;padding:0;box-sizing:border-box}
html,body{width:1200px;height:2752px;overflow:hidden}
body{position:relative;font-family:'Lato',sans-serif;color:var(--text);background:var(--white)}
.abs{position:absolute}
.btn{position:absolute;display:flex;align-items:center;justify-content:center;height:30px;width:125px;border-radius:15px;font-family:'Poppins',sans-serif;font-size:9px;font-weight:600;letter-spacing:.5px;text-transform:uppercase}
.btn-solid{background:var(--orange);color:var(--white)}
.btn-outline{border:2px solid var(--white);color:var(--white)}
h1,h2,h3,h4{font-family:'Poppins',sans-serif}

/* hero */
.hero{left:0;top:0;width:1200px;height:431px;background:linear-gradient(180deg,#3d3b38 0%,#5a5550 45%,#2f2d2b 100%)}
.hero-shade{left:0;top:0;width:1200px;height:431px;background:rgba(20,20,20,.45)}
.hero-kicker{left:0;top:36px;width:1200px;text-align:center;font-family:'Poppins',sans-serif;font-size:16px;font-weight:500;color:var(--white)}
.hero-title{left:0;top:84px;width:1200px;text-align:center;font-size:52px;line-height:56px;font-weight:700;color:var(--white)}
.hero-text{left:280px;top:224px;width:640px;text-align:center;font-size:11.5px;line-height:18px;color:var(--white)}
.hero-dots{left:958px;top:114px;width:8px}
.hero-dots span{display:block;width:7px;height:7px;border:1px solid var(--white);margin-bottom:8px}
.hero-dots span.on{background:var(--white)}

/* about */
.eyebrow{font-family:'Poppins',sans-serif;font-size:10px;font-weight:500;color:var(--blue);letter-spacing:.5px}
.about-eyebrow{left:239px;top:474px;width:352px;text-align:right}
.about-title{left:210px;top:494px;width:381px;text-align:right;font-size:25px;line-height:33px;font-weight:700;color:var(--ink)}
.about-text{left:239px;top:612px;width:352px;text-align:right;font-size:11px;line-height:17px}
.photo{background:linear-gradient(135deg,#c9ccd2,#6d7686)}
.photo-handshake{left:609px;top:477px;width:357px;height:237px;background:linear-gradient(135deg,#e4e6ea 0%,#9aa4b2 50%,#2f3d55 100%)}
.photo-meeting{left:235px;top:738px;width:356px;height:235px;background:linear-gradient(135deg,#6e6a66 0%,#d8dde3 45%,#8b97a6 100%)}
.who-eyebrow{left:609px;top:733px}
.who-text{left:609px;top:756px;width:357px;font-size:12px;line-height:17px;color:var(--ink)}

/* solutions */
.solutions{left:0;top:1018px;width:1200px;height:551px;background:var(--light)}
.section-title{left:0;width:1200px;text-align:center;font-size:25px;font-weight:700;color:var(--ink)}
.section-lead{left:330px;width:540px;text-align:center;font-size:11px;line-height:17px;color:var(--ink)}
.card{position:absolute;background:var(--white);box-shadow:0 4px 14px rgba(0,0,0,.06)}
.card-img{width:100%}
.card h3{position:absolute;left:24px;font-size:13px;font-weight:600;color:var(--ink)}
.card p{position:absolute;left:24px;width:190px;font-size:11px;line-height:18px;color:var(--ink)}
.svc{top:1174px;width:231px;height:345px}
.svc .card-img{height:175px}
.svc h3{top:196px}
.svc p{top:218px}
.svc .btn{left:24px;top:289px;width:96px;height:29px}

/* why */
.why-photo{left:0;top:1569px;width:591px;height:611px;background:linear-gradient(135deg,#dfe6ec 0%,#8da5c0 45%,#3e4b5e 100%)}
.why-panel{left:591px;top:1569px;width:609px;height:611px;background:var(--orange)}
.why-title{left:672px;top:1628px;font-size:27px;font-weight:700;color:var(--white)}
.why-item{position:absolute;left:672px;width:300px}
.why-item svg{position:absolute;left:0;top:4px}
.why-item h4{position:absolute;left:44px;top:0;font-size:16px;font-weight:600;color:var(--white);white-space:nowrap}
.why-item p{position:absolute;left:44px;top:26px;width:200px;font-size:11px;line-height:19px;color:var(--white)}

/* team */
.team{top:2336px;width:231px;height:310px}
.team .card-img{height:233px}
.portrait-a{background:linear-gradient(135deg,#8a6a58,#3a2b25)}
.portrait-b{background:linear-gradient(135deg,#f1ece6,#c89a7c)}
.portrait-c{background:linear-gradient(135deg,#c8c1b4,#4a4640)}
.team h3{top:254px}
.team p{top:274px}

/* footer */
.footer{left:0;top:2692px;width:1200px;height:60px;background:var(--footer)}
.copyright{left:235px;top:2719px;font-size:8px;color:var(--muted);letter-spacing:.3px}
.footer-nav{left:796px;top:2719px;font-size:8px;color:var(--muted);letter-spacing:.3px;display:flex;gap:28px}
</style>
</head>
<body>

<!-- hero -->
<div class="abs hero" role="img" aria-label="Photo of a team meeting in a glass-walled office"></div>
<div class="abs hero-shade"></div>
<div class="abs hero-kicker">Lorem Ipsum Dolor Sit World</div>
<h1 class="abs hero-title">We Create value Earlier<br>More Reliably</h1>
<p class="abs hero-text">Lorem ipsum dolor sit amet, consectetur adipiscing elit. Ut facilisis et enim id luctus. In hac habitasse platea dictumst. Vestibulum aliquam, urna ac vestibulum sagittis, est quam tincidunt sem, vitae faucibus nunc elit vel libero.</p>
<div class="btn btn-solid" style="left:468px;top:293px">Learn More</div>
<div class="btn btn-outline" style="left:607px;top:293px">Contact Us</div>
<div class="abs hero-dots"><span class="on"></span><span></span><span></span><span></span></div>

<!-- about -->
<div class="abs eyebrow about-eyebrow">ABOUT</div>
<h2 class="abs about-title">We Create Value Earlier More Reliably, Why &nbsp;We Best In Consulting</h2>
<p class="abs about-text">Lorem ipsum dolor sit amet, consectetur adipiscing elit. Ut facilisis et enim id luctus. In hac habitasse platea dictumst. Vestibulum aliquam, urna ac vestibulum sagittis, est quam tincidunt sem, vitae faucibus nunc elit vel libero.</p>
<div class="abs photo-handshake" role="img" aria-label="Photo of business people shaking hands"></div>
<div class="abs photo-meeting" role="img" aria-label="Photo of colleagues working around a meeting table"></div>
<div class="abs eyebrow who-eyebrow">WHO WE ARE</div>
<p class="abs who-text">Lorem ipsum dolor sit amet, consectetur adipiscing elit. Ut facilisis et enim id luctus. In hac habitasse platea dictumst. Vestibulum aliquam, urna ac vestibulum sagittis, est quam tincidunt sem, vitae faucibus nunc elit vel libero. Nulla facilisi. Etiam commodo cursus lobortis. Vestibulum ante ipsum primis in faucibus orci luctus et ultrices posuere cubilia Curae; Curabitur id semper justo, luctus dapibus lorem. Aliquam at diam ullamcorper, sagittis dui vel, ullamcorper nulla.</p>
<div class="btn btn-solid" style="left:609px;top:907px">Learn More</div>

<!-- solutions -->
<div class="abs solutions"></div>
<h2 class="abs section-title" style="top:1056px">We Have The Right Solutions</h2>
<p class="abs section-lead" style="top:1107px">Nulla facilisi. Etiam commodo cursus lobortis. Vestibulum ante ipsum primis in faucibus orci luctus et ultrices posuere cubilia Curae; Curabitur id semper justo, luctus dapibus lorem.</p>

<div class="card svc" style="left:235px">
  <div class="card-img" style="background:linear-gradient(135deg,#d9d6d0,#6d665e)" role="img" aria-label="Photo of designers at a laptop"></div>
  <h3>Graphic Design</h3>
  <p>Nulla facilisi. Etiam commodo cursus lobortis. Vestibulum ante ipsum primis in faucibus orci luctus etlorem.</p>
  <div class="btn btn-solid">Learn More</div>
</div>
<div class="card svc" style="left:484px">
  <div class="card-img" style="background:linear-gradient(135deg,#e9e7e3,#4a4744)" role="img" aria-label="Photo of a team presentation in an office"></div>
  <h3>Web Design</h3>
  <p>Nulla facilisi. Etiam commodo cursus lobortis. Vestibulum ante ipsum primis in faucibus orci luctus etlorem.</p>
  <div class="btn btn-solid">Learn More</div>
</div>
<div class="card svc" style="left:736px">
  <div class="card-img" style="background:linear-gradient(135deg,#9a9186,#3c3a37)" role="img" aria-label="Overhead photo of a team working at a table"></div>
  <h3>Web Development</h3>
  <p>Nulla facilisi. Etiam commodo cursus lobortis. Vestibulum ante ipsum primis in faucibus orci luctus etlorem.</p>
  <div class="btn btn-solid">Learn More</div>
</div>

<!-- why -->
<div class="abs why-photo" role="img" aria-label="Photo of two colleagues reviewing a tablet and documents"></div>
<div class="abs why-panel"></div>
<h2 class="abs why-title">Why You Choose Us?</h2>

<div class="why-item" style="top:1697px">
  <svg width="30" height="30" viewBox="0 0 30 30" fill="none" stroke="#fff" stroke-width="1.4"><rect x="3" y="4" width="20" height="22" rx="1"/><path d="M7 10h12M7 15h8M7 20h6"/><circle cx="23" cy="21" r="4"/></svg>
  <h4>Digital Marketing</h4>
  <p>Nulla facilisi. Etiam commodo cursus lobortis. Vestibulum ante ipsum primis in faucibus orci luctus etlorem.</p>
</div>
<div class="why-item" style="top:1809px">
  <svg width="30" height="30" viewBox="0 0 30 30" fill="none" stroke="#fff" stroke-width="1.4"><rect x="3" y="5" width="24" height="17" rx="1"/><path d="M10 26h10M15 22v4M8 17l5-5 4 3 5-6"/></svg>
  <h4>Digital Marketing</h4>
  <p>Nulla facilisi. Etiam commodo cursus lobortis. Vestibulum ante ipsum primis in faucibus orci luctus etlorem.</p>
</div>
<div class="why-item" style="top:1921px">
  <svg width="30" height="30" viewBox="0 0 30 30" fill="none" stroke="#fff" stroke-width="1.4"><rect x="3" y="3" width="24" height="16" rx="1"/><path d="M7 8h16M7 13h10"/><circle cx="10" cy="24" r="3"/><circle cx="20" cy="24" r="3"/></svg>
  <h4>Digital Marketing</h4>
  <p>Nulla facilisi. Etiam commodo cursus lobortis. Vestibulum ante ipsum primis in faucibus orci luctus etlorem.</p>
</div>
<div class="why-item" style="top:2033px">
  <svg width="30" height="30" viewBox="0 0 30 30" fill="none" stroke="#fff" stroke-width="1.4"><rect x="4" y="4" width="22" height="18" rx="2"/><path d="M8 9h14M8 13h14M8 17h8M11 22l-2 5M19 22l2 5"/></svg>
  <h4>Digital Marketing</h4>
  <p>Nulla facilisi. Etiam commodo cursus lobortis. Vestibulum ante ipsum primis in faucibus orci luctus etlorem.</p>
</div>

<!-- team -->
<h2 class="abs section-title" style="top:2218px">We Have The Right Solutions</h2>
<p class="abs section-lead" style="top:2270px">Nulla facilisi. Etiam commodo cursus lobortis. Vestibulum ante ipsum primis in faucibus orci luctus et ultrices posuere cubilia Curae; Curabitur id semper justo, luctus dapibus lorem.</p>

<div class="card team" style="left:235px">
  <div class="card-img portrait-a" role="img" aria-label="Portrait photo of a team member"></div>
  <h3>John Doe</h3>
  <p>Producer</p>
</div>
<div class="card team" style="left:484px">
  <div class="card-img portrait-b" role="img" aria-label="Portrait photo of a team member"></div>
  <h3>John Doe</h3>
  <p>Producer</p>
</div>
<div class="card team" style="left:736px">
  <div class="card-img portrait-c" role="img" aria-label="Portrait photo of a team member"></div>
  <h3>John Doe</h3>
  <p>Producer</p>
</div>

<!-- footer -->
<div class="abs footer"></div>
<div class="abs copyright">© 2018 ZORVEL ANALYTICS. ALL RIGHTS RESERVED.</div>
<nav class="abs footer-nav"><span>HOME</span><span>ABOUT US</span><span>CONTACT US</span></nav>

</body>
</html>
```